Need UI Design for HRIS/Company Employee Portal

Currently have a custom built system that we hire and use as our employee database and employee portal for everyone in our company. The software has evolved dramatically and needs to be completely user friendly and aesthetically pleasing. Attached are a few ideas and pages we already have. Please make 5 designs for the 5 different pages below. Would need all specifications of content used, color code, font/typography, icons used, etc. We can pretty much pull any information from anywhere we have for example, employee photo, address, DOB, Hire date, Title, ETC.

-Company Staff/Admin Welcome Page
- We want quick shortcuts/buttons or icons for staff functions, such as terminate, hire, information change, reports, etc
-Employee Profile Welcome Page
- We want quick shortcuts/buttons or icons for direct deposit, time off request, information change, pay stubs
-List of Applications/Candidates Page
-Profile Search Page
-Manage Inventory

Target Market(s)

Employees

Industry/Entity Type

It Company

Coding

Coded - Design and coding required

Number of Pages Required

5+ page

Font styles to use
Sans Serif

Requirements
Must have
• Must be professional! Aesthetics, Icons, Easy User Interface, Modern New technology look, can be responsive to mobile
Should not have
• Nothing old school

```html
<!DOCTYPE html>
<html lang="en">
<head>
<meta charset="utf-8">
<title>Employee Profile – Harbor Shield Services</title>
<link rel="stylesheet" href="https://fonts.googleapis.com/css2?family=Open+Sans:ital,wght@0,400;0,600;0,700;1,400&display=swap">
<style>
  :root {
    --bg: #e6e6e6;
    --panel: #ffffff;
    --nav: #4d7ce0;
    --button: #5a80e2;
    --cal-head: #6287e4;
    --cal-arrow: #55659f;
    --accent: #5a7fd6;
    --text: #8a8a8a;
    --text-dark: #7a7a7a;
    --muted-cell: #d0d0d0;
    --avatar: #7b98e0;
    --white: #ffffff;
  }
  * { box-sizing: border-box; margin: 0; padding: 0; }
  html, body {
    width: 814px; height: 1200px; overflow: hidden;
    background: var(--bg);
    font-family: "Open Sans", Arial, sans-serif;
    color: var(--text);
  }
  .page {
    position: relative; width: 768px; height: 1132px;
    transform: scale(1.0599); transform-origin: 0 0;
  }
  .abs { position: absolute; }
  .panel { position: absolute; background: var(--panel); }

  /* header */
  .brand { left: 18px; top: 46px; display: flex; align-items: center; gap: 8px; }
  .brand-mark { width: 16px; height: 16px; background: var(--nav); }
  .brand-name { font-size: 12px; font-weight: 700; color: var(--nav); letter-spacing: .3px; text-transform: uppercase; }
  .search { left: 493px; top: 37px; width: 177px; height: 32px; background: var(--white);
    font-size: 14px; color: #666; padding: 7px 11px; }
  .icon-btn { top: 37px; width: 32px; height: 32px; background: var(--button);
    display: flex; align-items: center; justify-content: center; }
  .search-btn { left: 670px; }
  .power-btn { left: 718px; }

  .nav { left: 0; top: 97px; width: 768px; height: 32px; background: var(--nav);
    display: flex; align-items: center; padding-left: 18px; gap: 25px; }
  .nav a { color: var(--white); font-size: 12.5px; text-decoration: none; }

  /* profile side */
  .profile-card { left: 18px; top: 150px; width: 136px; height: 191px; }
  .avatar { width: 136px; height: 136px; background: var(--avatar); }
  .status { padding: 6px 7px 0; font-size: 10px; }
  .row { display: flex; justify-content: space-between; line-height: 15px; }
  .row .label { color: var(--accent); font-weight: 700; }
  .row .value { color: var(--text); }
  .row .value.strong { font-weight: 700; }
  .hours { text-align: center; font-size: 10px; margin-top: 1px; }

  .id-card { left: 18px; top: 361px; width: 136px; height: 192px; padding: 7px 7px; font-size: 10px; }
  .id-group + .id-group { margin-top: 15px; }
  .id-title { font-weight: 700; color: var(--text); line-height: 13px; }
  .id-card .row { line-height: 15px; }

  /* main card */
  .main-card { left: 175px; top: 150px; width: 575px; height: 192px; padding: 12px 14px; }
  .name { font-size: 15px; font-weight: 700; color: var(--accent); }
  .address { margin-top: 18px; font-size: 11px; font-style: italic; line-height: 16.5px; }
  .contact { margin-top: 22px; font-size: 11px; line-height: 16.5px; font-weight: 700; color: var(--text-dark); }
  .contact .label { color: var(--accent); }
  .action-btn { position: absolute; left: 405px; width: 157px; height: 32px; background: var(--button);
    color: var(--white); font-weight: 700; font-size: 13px; display: flex; align-items: center; justify-content: center; }
  .rehire { top: 14px; }
  .terminate { top: 60px; }

  .message { left: 175px; width: 575px; height: 86px; padding: 8px 16px 8px 12px; }
  .message h2 { font-size: 13px; font-weight: 700; color: var(--accent); line-height: 18px; }
  .message p { font-size: 11.5px; line-height: 17px; color: var(--text); }
  .employee-message { top: 361px; }
  .company-message { top: 468px; }

  /* calendar */
  .cal-head { left: 175px; top: 576px; width: 575px; height: 37px; background: var(--cal-head);
    color: var(--white); font-size: 15px; font-weight: 700; display: flex; align-items: center; justify-content: center; }
  .cal-arrow { position: absolute; top: 4px; width: 29px; height: 29px; border-radius: 50%; background: var(--cal-arrow);
    display: flex; align-items: center; justify-content: center; }
  .cal-arrow.prev { left: 5px; }
  .cal-arrow.next { right: 5px; }
  .weekdays { left: 175px; top: 621px; width: 575px; display: grid; grid-template-columns: repeat(7, 76px); column-gap: 7.2px;
    font-size: 13.5px; font-weight: 700; color: #b4b4b4; text-align: center; }
  .days { left: 175px; top: 647px; width: 575px; display: grid; grid-template-columns: repeat(7, 76px);
    grid-auto-rows: 76px; column-gap: 7.2px; row-gap: 7.2px; }
  .day { background: var(--panel); font-size: 14px; font-weight: 700; color: var(--text); padding: 3px 7px; }
  .day.empty { background: var(--muted-cell); }

  .footer { left: 18px; top: 1076px; width: 732px; height: 32px; padding: 0 10px;
    display: flex; align-items: center; font-size: 12.5px; font-weight: 700; color: var(--text-dark); }
  .footer .links { margin-left: auto; display: flex; gap: 28px; }
  .footer a { color: var(--accent); text-decoration: none; }
</style>
</head>
<body>
<div class="page">

  <header>
    <div class="abs brand">
      <span class="brand-mark"></span>
      <span class="brand-name">Harbor Shield Services, Inc.</span>
    </div>
    <div class="abs search">Search</div>
    <div class="abs icon-btn search-btn" aria-label="Search">
      <svg width="14" height="14" viewBox="0 0 14 14" fill="none" stroke="#fff" stroke-width="2">
        <circle cx="5.5" cy="5.5" r="4"/><line x1="8.5" y1="8.5" x2="13" y2="13" stroke-linecap="round"/>
      </svg>
    </div>
    <div class="abs icon-btn power-btn" aria-label="Log out">
      <svg width="16" height="16" viewBox="0 0 16 16" fill="none" stroke="#fff" stroke-width="2" stroke-linecap="round">
        <path d="M4.6 4.2a6 6 0 1 0 6.8 0"/><line x1="8" y1="1.5" x2="8" y2="7.5"/>
      </svg>
    </div>
    <nav class="abs nav">
      <a href="#">Home</a><a href="#">Personal Licenses</a><a href="#">Forms\Requests</a><a href="#">Team Contacts</a>
      <a href="#">Benefits</a><a href="#">Training</a><a href="#">Equipment</a><a href="#">Help</a>
    </nav>
  </header>

  <aside>
    <section class="panel profile-card">
      <div class="avatar" role="img" aria-label="Employee profile photo"></div>
      <div class="status">
        <div class="row"><span class="label">Status:</span><span class="value strong">Active</span></div>
        <div class="row"><span class="label">Hire Date:</span><span class="value strong">15 Mar 16</span></div>
        <div class="hours">17 Hours</div>
      </div>
    </section>

    <section class="panel id-card">
      <div class="id-group">
        <div class="id-title">GUARD CARD</div>
        <div class="row"><span class="label">SSN:</span><span class="value">5555</span></div>
        <div class="row"><span class="label">ID:</span><span class="value">123456789</span></div>
        <div class="row"><span class="label">Expire:</span><span class="value">27 Mar 18</span></div>
      </div>
      <div class="id-group">
        <div class="id-title">STATE ID</div>
        <div class="row"><span class="label">ID:</span><span class="value">123456789</span></div>
        <div class="row"><span class="label">Expire:</span><span class="value">27 Mar 18</span></div>
      </div>
      <div class="id-group">
        <div class="id-title">DRIVER LICENSE</div>
        <div class="row"><span class="label">ID:</span><span class="value">123456789</span></div>
        <div class="row"><span class="label">Expire:</span><span class="value">28 Mar 18</span></div>
      </div>
    </section>
  </aside>

  <main>
    <section class="panel main-card">
      <h1 class="name">Alan Hewitt</h1>
      <div class="address">14 Elm Lane<br>Fairview<br>NY 55512</div>
      <div class="contact">
        <div><span class="label">Tel:</span> 555-20841</div>
        <div><span class="label">Mobile:</span> 07700900412</div>
        <div><span class="label">E-Mail:</span> alan.hewitt@example.com</div>
      </div>
      <div class="action-btn rehire">Re-Hire</div>
      <div class="action-btn terminate">Terminate</div>
    </section>

    <section class="panel message employee-message">
      <h2>Employee Message</h2>
      <p>Morbi mattis tortor mauris, nec iaculis est tincidunt ut. Nulla sit amet libero sit amet lectus blandit eleifend. Praesent luctus est sit amet sodales placerat. Integer a libero eu velit facilisis dignissim convallis facilisis odio. Duis fringilla, metus in auctor tempor, justo augue viverra velit, t nunc.</p>
    </section>

    <section class="panel message company-message">
      <h2>Company Message</h2>
      <p>Morbi mattis tortor mauris, nec iaculis est tincidunt ut. Nulla sit amet libero sit amet lectus blandit eleifend. Praesent luctus est sit amet sodales placerat. Integer a libero eu velit facilisis dignissim convallis facilisis odio. Duis fringilla, metus in auctor tempor, justo augue viverra velit, t nunc.</p>
    </section>

    <section class="calendar">
      <div class="abs cal-head">
        <span class="cal-arrow prev"><svg width="10" height="10" viewBox="0 0 10 10" fill="none" stroke="#fff" stroke-width="2"><path d="M6.5 1.5 3 5l3.5 3.5"/></svg></span>
        September 2017
        <span class="cal-arrow next"><svg width="10" height="10" viewBox="0 0 10 10" fill="none" stroke="#fff" stroke-width="2"><path d="M3.5 1.5 7 5 3.5 8.5"/></svg></span>
      </div>
      <div class="abs weekdays">
        <span>MON</span><span>TUES</span><span>WED</span><span>THU</span><span>FRI</span><span>SAT</span><span>SUN</span>
      </div>
      <div class="abs days">
        <div class="day empty"></div><div class="day empty"></div><div class="day empty"></div>
        <div class="day">1</div><div class="day">2</div><div class="day">3</div><div class="day">4</div>
        <div class="day">5</div><div class="day">6</div><div class="day">7</div><div class="day">8</div><div class="day">9</div><div class="day">10</div><div class="day">11</div>
        <div class="day">12</div><div class="day">13</div><div class="day">14</div><div class="day">15</div><div class="day">16</div><div class="day">17</div><div class="day">18</div>
        <div class="day">19</div><div class="day">20</div><div class="day">21</div><div class="day">22</div><div class="day">23</div><div class="day">24</div><div class="day">25</div>
        <div class="day">26</div><div class="day">27</div><div class="day">28</div><div class="day">29</div><div class="day">30</div>
        <div class="day empty"></div><div class="day empty"></div>
      </div>
    </section>
  </main>

  <footer class="panel footer">
    <span>© 2016&nbsp; HSS</span>
    <span class="links"><a href="#">Legal</a><a href="#">Terms</a></span>
  </footer>

</div>
</body>
</html>
```